One-Page Designed - Top 5 Tips for Curly Hair

I need a one-pager designed that looks friendly, informative, and natural, but that can be used as a PDF download for a website. the current website is not launched yet but the link is www.fernloftstudio.example for reference.

This piece will be the piece we send to clients once they log into our website and subscribe so it is a very important piece.

Fern Salon is an eco-friendly and holistically minded salon. Through research and education, we’ve curated a selection of less toxic hair color and hair styling products that offer professional results with the most natural ingredients on the market today. Whether you’re looking for a great haircut, expert grey coverage, bouncy curls or an amazing balayage, we’re here for you.

We’re dedicated to improving the locks of curly girls in the greater Boston area. We are curly hair experts who are committed to continuing education on the lasted curly hair cutting and coloring techniques. We’ll keep your curls healthy and fabulous with our carefully curated collection of products too.

Target Market(s)

Curly Hair Girls Who Want to Go to Natural Product Salon

Industry/Entity Type

Hair And Beauty

Font styles to use
Other font styles liked:
• Dancing Script and Arial Nova

Requirements
Must have
• Should have graphics that call out the tips and then have the blocks that go with them as the descriptions. Should be fun, friendly and informative. Final product should be send as a PDF.
• Colors should go with Hex: #5BC2E7 and Hex: #686A66 and Hex: #C8C9C7
• It should include their logo and a photo of the owner Marisol.
Nice to have
• Images that reflect the copy.

```html
<!DOCTYPE html>
<html lang="en">
<head>
<meta charset="utf-8">
<title>Top 5 Tips for Curly Hair – Fern Salon</title>
<link rel="stylesheet" href="https://fonts.googleapis.com/css2?family=Arimo:wght@400;700&family=Dancing+Script:wght@400;700&family=Roboto+Condensed:wght@300;400;700&display=swap">
<style>
  :root {
    --sky: #4DC3ED;
    --brand-blue: #5BC2E7;
    --slate: #686A66;
    --stone: #B3B3B3;
    --mist: #C8C9C7;
    --backdrop: #3B3B3D;
    --white: #FFFFFF;
  }
  * { margin: 0; padding: 0; box-sizing: border-box; }
  html, body { width: 1200px; height: 1200px; overflow: hidden; background: var(--backdrop); }
  .sheet {
    position: absolute; left: 261px; top: 119.5px;
    width: 1000px; height: 1414px;
    transform: scale(0.679); transform-origin: 0 0;
    background: var(--white); overflow: hidden;
    font-family: "Arimo", Arial, sans-serif;
  }
  .top-band { position: absolute; left: 0; top: 0; width: 1000px; height: 21px; background: var(--sky); }
  .hero-photo {
    position: absolute; left: 0; top: 21px; width: 1000px; height: 700px;
    background: linear-gradient(90deg, #FFFFFF 0%, #F3F8FB 40%, #E9F1F6 60%, #D9E4EC 100%);
  }
  .hero-photo .subject {
    position: absolute; left: 590px; top: 60px; width: 410px; height: 640px;
    background: radial-gradient(ellipse at 55% 55%, #D8302F 0%, #C95A45 35%, rgba(120,80,60,0.35) 65%, rgba(233,241,246,0) 80%);
  }
  .logo {
    position: absolute; left: 634px; top: 56px;
    font-family: "Arimo", Arial, sans-serif; font-weight: 700; font-size: 60px;
    letter-spacing: 2px; color: var(--brand-blue); white-space: nowrap;
  }
  .grey-panel { position: absolute; left: 0; top: 0; width: 1000px; height: 1414px; }
  .headline-arc { position: absolute; left: 0; top: 0; width: 1000px; height: 700px; }
  .title {
    position: absolute; left: 138px; top: 318px;
    font-weight: 700; font-size: 70px; line-height: 58px; letter-spacing: -3px;
    color: var(--brand-blue); white-space: nowrap;
  }
  .intro {
    position: absolute; left: 143px; top: 454px;
    font-size: 24px; line-height: 28.5px; color: var(--slate); white-space: nowrap;
  }
  .tip { position: absolute; left: 0; width: 1000px; }
  .tip-label {
    position: absolute; right: 736px; text-align: right; white-space: nowrap;
    font-family: "Dancing Script", cursive; font-weight: 700; font-size: 21px; line-height: 24px;
    color: var(--white);
  }
  .tip-body {
    position: absolute; left: 280px; top: 0; white-space: nowrap;
    font-family: "Roboto Condensed", "Arial Narrow", sans-serif; font-weight: 300;
    font-size: 15.4px; line-height: 20px; color: var(--white);
  }
  .divider {
    position: absolute; left: 130px; width: 740px; height: 0;
    border-top: 2px dashed rgba(255,255,255,0.55);
  }
  .footer-band { position: absolute; left: 0; top: 1260px; width: 1000px; height: 154px; background: var(--sky); }
  .owner-photo {
    position: absolute; left: 77px; top: 1219px; width: 180px; height: 180px; border-radius: 50%;
    border: 4px solid var(--sky);
    background: radial-gradient(circle at 50% 45%, #E8C4AE 0%, #B98A74 35%, #4A2E24 70%, #2A1A15 100%);
  }
  .byline {
    position: absolute; left: 275px; top: 1278px; white-space: nowrap;
    font-family: "Dancing Script", cursive; font-size: 29px; color: var(--white);
  }
  .bio {
    position: absolute; left: 275px; top: 1318px; white-space: nowrap;
    font-family: "Roboto Condensed", "Arial Narrow", sans-serif; font-weight: 300;
    font-size: 16.5px; line-height: 21px; color: var(--white);
  }
  .contact {
    position: absolute; left: 275px; top: 1368px;
    font-family: "Arimo", Arial, sans-serif; font-weight: 700; font-size: 10.5px;
    letter-spacing: 4.2px; color: var(--white); text-transform: uppercase; white-space: nowrap;
  }
</style>
</head>
<body>
<main class="sheet">
  <div class="top-band"></div>

  <div class="hero-photo" role="img" aria-label="Photo of a smiling curly-haired woman in a red top and sunglasses taking a selfie against a bright waterfront sky">
    <div class="subject"></div>
  </div>

  <div class="logo">Fern Salon</div>

  <svg class="grey-panel" viewBox="0 0 1000 1414" aria-hidden="true">
    <polygon points="0,639 1000,707 1000,1260 0,1260" fill="#B3B3B3"/>
  </svg>

  <svg class="headline-arc" viewBox="0 0 1000 700">
    <path d="M0,420 C40,300 140,200 250,196 C310,194 360,220 388,262" fill="none" stroke="#4DC3ED" stroke-width="6"/>
    <path id="arc-line" d="M62,425 C85,330 150,245 240,228 C300,218 350,240 390,285" fill="none"/>
    <text font-family="Dancing Script, cursive" font-size="66" fill="#4DC3ED">
      <textPath href="#arc-line">A Curly Stylists'</textPath>
    </text>
  </svg>

  <h1 class="title">Top 5 Tips for<br>Curly Hair</h1>

  <p class="intro">I get it. Everyone is looking for ease and<br>order in their busy lives.&nbsp; Whether you’ve<br>just ditched your flat iron or you’re a<br>long-time curly girl looking for fresh<br>direction, here are our top tips for luscious<br>curls and waves.</p>

  <section class="tip" style="top:709px">
    <h2 class="tip-label">Embrace the<br>diversity of your<br>curls</h2>
    <p class="tip-body">Yes, you will have “curl diversity” everyday and that’s okay. Being consistent with your haircare<br>routine and avoiding the temptation to blow dry or straighten will do wonders for your hair over<br>the long term. I promise, your overall curl or wave pattern will improve over time. I also promise<br>that you will never have the same head of curls twice. Variety is the spice of life!</p>
  </section>
  <div class="divider" style="top:799px"></div>

  <section class="tip" style="top:813px">
    <h2 class="tip-label">Keep your cleanser<br>gentle and leave in a<br>little bit of your<br>conditioner</h2>
    <p class="tip-body" style="top:2px">Yes, you will have “curl diversity” everyday and that’s okay. Being consistent with your haircare<br>routine and avoiding the temptation to blow dry or straighten will do wonders for your hair over<br>the long term. I promise, your overall curl or wave pattern will improve over time. I also promise<br>that you will never have the same head of curls twice. Variety is the spice of life!</p>
  </section>
  <div class="divider" style="top:909px"></div>

  <section class="tip" style="top:925px">
    <h2 class="tip-label">Avoid silicones and<br>sulfates</h2>
    <p class="tip-body">You’ve heard this (pretty much everywhere) before but that’s only because it’s true. Silicones coat<br>the hair and are extremely difficult to remove, leaving the hair with an altered texture and<br>rendering it impervious to deep conditioning.&nbsp; Use only reputable hair care products like those<br>from Meadowleaf Organics or Coil Harbor. Beware of hidden silicones. They can be in the<br>“fragrance” portion of the ingredient list. (thanks to Delia Ashcombe for that new knowledge.</p>
  </section>
  <div class="divider" style="top:1039px"></div>

  <section class="tip" style="top:1053px">
    <h2 class="tip-label">Rest easy</h2>
    <p class="tip-body">Wrap your curls or waves in a silk scarf to avoid friction. If you’re rough sleeper and you wake up with<br>your scarf wrapped somewhere between your neck and your armpit (me), a silk pillow case is a better<br>and safer option. Less friction= smoother curls.</p>
  </section>
  <div class="divider" style="top:1131px"></div>

  <section class="tip" style="top:1149px">
    <h2 class="tip-label">Cutting curls every<br>6-10 weeks</h2>
    <p class="tip-body">I’m not saying this because I’m a stylist, I swear. I’m saying this because I care about curly hair.<br>Cutting curls every 6-10 weeks, depending on the length and curl type is essential to great hair<br>health. Keeping your ends blunt and free of splits and frays will make styling easier and is<br>especially important of you’re growing your hair longer. We all know how long that takes when<br>you’re a curly girl.</p>
  </section>

  <footer class="footer-band"></footer>
  <div class="owner-photo" role="img" aria-label="Portrait photo of salon owner Marisol Quintero"></div>
  <p class="byline">By Marisol Quintero</p>
  <p class="bio">Marisol is the owner of Fern Salon in Ashvale and Millbrook, ME. She is a Verra advanced curly hair stylist<br>and is certified in the Ring by Ring method. She is a curl advocate and a lover of natural and organic products.</p>
  <p class="contact">www.fernloftstudio.example &nbsp;~hello@fernloftstudio.example</p>
</main>
</body>
</html>
```